3 point buck deer with toolbelt

I would like to have a logo that has a 3 point buck deer as a handyman/tuff guy with a tool belt on, flexing and holding a hammer.

Target Market(s)

homeowners

Industry/Entity Type

Handyman

Contact Information for Business Card

Ridgeway Builders; Dalton R. Merrow; 4817 Larkspur Ct., Leavenworth, Wa 98734; 425.555.0147; ridgewaybuilders@mailnest.example

Font styles to use
Serif

Requirements
Must have
• a 3 point buck deer with a toolbelt
Nice to have
• hammer, broom, saw
Should not have
• the color pink

```html
<!DOCTYPE html>
<html lang="en">
<head>
<meta charset="utf-8">
<title>Ridgeway Builders — Business Card</title>
<link rel="stylesheet" href="https://fonts.googleapis.com/css2?family=Marcellus&family=Crimson+Pro:wght@400;600&display=swap">
<style>
  :root {
    --card-bg: #ffffff;
    --navy: #283593;
    --navy-deep: #10153f;
    --ink: #1a1a1a;
    --rule: #9a9a9a;
    --mark-grey-light: #f1f1f1;
    --mark-grey: #dcdcdc;
  }
  * { margin: 0; padding: 0; box-sizing: border-box; }
  html, body {
    width: 1200px;
    height: 703px;
    overflow: hidden;
    background: var(--card-bg);
  }
  .card {
    position: relative;
    width: 1200px;
    height: 703px;
    background: var(--card-bg);
    overflow: hidden;
    font-family: "Crimson Pro", Georgia, serif;
    color: var(--ink);
  }
  .holder-name {
    position: absolute;
    left: 407px;
    top: 134px;
    font-size: 34px;
    font-weight: 400;
  }
  .brand-mark {
    position: absolute;
    left: 92px;
    top: 270px;
    width: 220px;
    display: flex;
    flex-direction: column;
    align-items: center;
    gap: 18px;
  }
  .brand-mark__dot {
    width: 70px;
    height: 70px;
    border-radius: 50%;
    background: var(--navy);
  }
  .brand-mark__name {
    font-family: "Crimson Pro", Georgia, serif;
    font-weight: 600;
    font-size: 36px;
    line-height: 1.1;
    text-align: center;
    color: var(--navy);
  }
  .company {
    position: absolute;
    left: 407px;
    top: 308px;
    font-family: "Marcellus", Georgia, serif;
    font-size: 49px;
    letter-spacing: 0.5px;
    color: var(--navy);
    white-space: nowrap;
  }
  .divider {
    position: absolute;
    left: 407px;
    top: 392px;
    width: 582px;
    border-top: 3px dotted var(--rule);
  }
  .contact {
    position: absolute;
    left: 407px;
    top: 410px;
    font-size: 33px;
    line-height: 45px;
  }
  .contact__email { margin-top: 10px; }
  .accent-figure {
    position: absolute;
    left: 1020px;
    top: 205px;
    width: 180px;
    height: 305px;
    border-radius: 90px 0 0 90px;
    background: linear-gradient(160deg, var(--mark-grey-light), var(--mark-grey));
    opacity: 0.7;
  }
  .base-band {
    position: absolute;
    left: 0;
    bottom: 0;
    width: 1200px;
    height: 44px;
    background: linear-gradient(90deg, var(--navy-deep) 0%, var(--navy) 50%, var(--navy-deep) 100%);
  }
</style>
</head>
<body>
  <div class="card">
    <div class="holder-name">Dalton R. Merrow</div>

    <div class="brand-mark">
      <div class="brand-mark__dot"></div>
      <div class="brand-mark__name">Ridgeway<br>Builders</div>
    </div>

    <div class="company">RIDGEWAY BUILDERS</div>
    <div class="divider"></div>

    <div class="contact">
      <div>4817 Larkspur Ct., Leavenworth,</div>
      <div>Wa 98734, Phone : 425.555.0147</div>
      <div class="contact__email">Email : ridgewaybuilders@mailnest.example</div>
    </div>

    <div class="accent-figure" role="img" aria-label="Faint grey illustration of a buck deer holding a saw"></div>

    <div class="base-band"></div>
  </div>
</body>
</html>
```